New business card for my lawn and landscape business

Dorrin Yard and Building is a full-service lawn care, landscaping, and light construction company serving Paragould and the Northeast Arkansas region. The business is owned and operated by Marcus Toller, with a reputation for hands-on, detail-oriented service, dependable crews, and quality results for both residential and commercial clients. A well regarded business with great reviews.
Owner Marcus Toller
Dorrinyardandbuilding.example

Target Market(s)

Commercial, Middle, and upper class in north east Arkansas

Industry/Entity Type

Lawn maintenance and landscape

Contact Information for Business Card

Dorrin Yard And Building Professional lawn care, landscaping, and property improvement in Northeast Arkansas. • lawn maintenance •lawn treatments and weed control • exterior projects • Custom landscape design & installation • Sod, trees, rock & drainage solutions • Residential & commercial services Reliable. Detailed. Done right.

Requirements
Must have
• Business name, service area, list of some of our services, clean design that represents
Nice to have
• Unique. Different design element than just grass because its already in n the logo. Picture of a warm season (south) lawn or landscape. Pictures of the type of work we do

```html
<!DOCTYPE html>
<html lang="en">
<head>
<meta charset="utf-8">
<title>Dorrin Yard and Building – Business Card</title>
<link href="https://fonts.googleapis.com/css2?family=Montserrat:wght@600;700&family=Poppins:wght@400;600;700&family=Cinzel:wght@700&display=swap" rel="stylesheet">
<style>
  :root {
    --brand-green: #6fa638;
    --brand-green-light: #86b954;
    --ink: #2b2b2b;
    --steel: #8a8b8d;
    --card-white: #ffffff;
    --page-bg: #e9eaeb;
  }
  * { margin: 0; padding: 0; box-sizing: border-box; }
  html, body {
    width: 1093px; height: 1200px; overflow: hidden;
    background: var(--page-bg);
  }
  .card {
    position: absolute; left: 265px;
    width: 578px; height: 356px;
    border-radius: 26px; overflow: hidden;
  }
  .card--front { top: 226px; background: var(--card-white); }
  .card--back { top: 621px; background: var(--brand-green); color: #fff; text-align: center; }

  /* front */
  .brand {
    position: absolute; left: 42px; top: 128px;
    width: 236px; height: 100px;
    display: flex; align-items: center; gap: 12px;
  }
  .brand-mark {
    flex: none; width: 66px; height: 66px;
    border-radius: 50%;
    border: 6px solid var(--steel);
  }
  .brand-name {
    font-family: "Poppins", sans-serif; font-weight: 600;
    font-size: 20px; line-height: 24px;
    color: var(--brand-green); white-space: nowrap;
  }
  .divider {
    position: absolute; left: 288px; top: 74px;
    width: 2px; height: 209px;
    background: linear-gradient(to bottom, transparent, #9a9a9a 15%, #9a9a9a 85%, transparent);
  }
  .contact-block { position: absolute; left: 311px; top: 92px; }
  .person-name {
    font-family: "Montserrat", sans-serif; font-weight: 700;
    font-size: 21px; letter-spacing: 0.3px; line-height: 24px;
    color: var(--brand-green);
  }
  .person-role {
    font-family: "Poppins", sans-serif; font-size: 17px; line-height: 19px;
    color: var(--ink);
  }
  .contact-list { list-style: none; margin-top: 13px; }
  .contact-list li {
    display: flex; align-items: center; gap: 8px;
    font-family: "Poppins", sans-serif; font-size: 17px; line-height: 21px;
    color: var(--ink);
  }
  .contact-list svg { width: 15px; height: 15px; flex: none; }
  .contact-list .accent { color: var(--brand-green); }
  .address {
    margin-top: 13px;
    font-family: "Poppins", sans-serif; font-size: 17px; line-height: 21px;
    color: var(--ink);
  }

  /* back */
  .back-grass {
    position: absolute; left: 0; bottom: 0; width: 100%; height: 110px;
    background: linear-gradient(to bottom, rgba(134,185,84,0), rgba(134,185,84,0.75));
  }
  .back-content { position: relative; padding-top: 51px; }
  .company-title {
    font-family: "Montserrat", sans-serif; font-weight: 600;
    font-size: 24px; letter-spacing: 0.9px; line-height: 28px;
  }
  .company-summary {
    font-family: "Poppins", sans-serif; font-size: 17.5px; line-height: 21px;
    width: 480px; margin: 0 auto;
  }
  .rule { width: 482px; height: 1px; background: #fff; margin: 7px auto 0; }
  .service-list {
    list-style: none; margin: 9px 0 12px;
    font-family: "Cinzel", serif; font-weight: 700;
    font-size: 17px; line-height: 21px; letter-spacing: 0.3px;
  }
  .tagline {
    margin-top: 6px;
    font-family: "Poppins", sans-serif; font-weight: 700;
    font-size: 28px; line-height: 34px; letter-spacing: -0.3px;
  }
</style>
</head>
<body>

<section class="card card--front">
  <div class="brand">
    <div class="brand-mark"></div>
    <div class="brand-name">Dorrin Yard<br>and Building</div>
  </div>
  <div class="divider"></div>
  <div class="contact-block">
    <h1 class="person-name">MARCUS TOLLER</h1>
    <p class="person-role">Owner</p>
    <ul class="contact-list">
      <li>
        <svg viewBox="0 0 16 16"><path d="M3 1.5l2.5 0 1.2 3.3-1.6 1.3c.8 1.8 2.2 3.2 4 4l1.3-1.6 3.3 1.2v2.5c0 .9-.8 1.6-1.7 1.5C6.5 13.3 2.7 9.5 1.5 4.2 1.4 3.3 2.1 1.5 3 1.5z" fill="none" stroke="#6fa638" stroke-width="1.6"/></svg>
        044-123 456 789
      </li>
      <li>
        <svg viewBox="0 0 16 16"><rect x="1" y="3" width="14" height="10" fill="#6fa638"/><path d="M1 3l7 6 7-6" fill="none" stroke="#fff" stroke-width="1.2"/></svg>
        info@webname.com
      </li>
      <li>
        <svg viewBox="0 0 16 16"><g fill="none" stroke="#6fa638" stroke-width="1.3"><circle cx="8" cy="8" r="6.5"/><ellipse cx="8" cy="8" rx="3" ry="6.5"/><path d="M1.5 8h13M2.5 4.8h11M2.5 11.2h11"/></g></svg>
        <span>www.<span class="accent">websitename</span>.com</span>
      </li>
    </ul>
    <p class="address">421, Address line goes here<br>45452,Country Name</p>
  </div>
</section>

<section class="card card--back">
  <div class="back-grass" role="img" aria-label="Soft field of grass blades along the bottom of the card"></div>
  <div class="back-content">
    <h2 class="company-title">DORRIN YARD AND BUILDING</h2>
    <p class="company-summary">Professional lawn care, landscaping and property improvement in Northeast Arkansas.</p>
    <div class="rule"></div>
    <ul class="service-list">
      <li>Lawn maintenance</li>
      <li>Lawn treatments and weed control</li>
      <li>Exterior projects</li>
      <li>Custom landscape design &amp; installation</li>
      <li>Sod, trees, rock &amp; drainage solutions</li>
      <li>Residential &amp; commercial services</li>
    </ul>
    <div class="rule"></div>
    <p class="tagline">RELIABLE. DETAILED. DONE RIGHT</p>
  </div>
</section>

</body>
</html>
```